Wedding invitation

We need a wedding invitation designed with a logo using our initials and name underneath.
We are getting married at THE VERDELLE hotel in Gstaad and we would like have our logo similar to theirs but incorporating our initials n&l (any font/case) and our names below nuriya and Laurent. The Verdelle logo can be seen on their website.
The invitation would be square with the logo on the front in stamped foil and the colour would be THE VERDELLE brown (I have the exact colour)
THE VERDELLE Brown: C45 M70 Y68 K77
THE VERDELLE Rose Gold: BRENVIK 812
Inside we would have the invitation wording and on the opposite side some contact info. There would be four inserts - accom, directions, brunch and RSVP. We will provide the wording.

```html
<!DOCTYPE html>
<html lang="en">
<head>
<meta charset="utf-8">
<title>Nuriya and Laurent – Wedding Invitation</title>
<link href="https://fonts.googleapis.com/css2?family=Cormorant+SC:wght@500&family=Jost:wght@500&family=Pinyon+Script&display=swap" rel="stylesheet">
<style>
  :root {
    --ink: #1d1d1d;
    --paper: #ffffff;
    --rule: #8a8a8a;
  }
  html, body {
    margin: 0;
    padding: 0;
    width: 1200px;
    height: 606px;
    overflow: hidden;
    background: var(--paper);
    color: var(--ink);
  }
  .spread {
    position: relative;
    width: 1200px;
    height: 606px;
  }
  .invitation-panel {
    position: absolute;
    left: 2px;
    top: 2px;
    width: 566px;
    height: 584px;
    border: 1px solid var(--rule);
    box-sizing: border-box;
    text-align: center;
  }
  .front-panel {
    position: absolute;
    left: 620px;
    top: 0;
    width: 560px;
    height: 606px;
    text-align: center;
  }
  .monogram-mark {
    position: absolute;
    left: 50%;
    transform: translateX(-50%);
  }
  .invitation-panel .monogram-mark { top: 10px; width: 56px; height: 56px; }
  .front-panel .monogram-mark { top: 132px; width: 164px; height: 164px; }
  .couple-name {
    position: absolute;
    left: 0;
    right: 0;
    margin: 0;
    font-family: "Jost", sans-serif;
    font-weight: 500;
    color: var(--ink);
    white-space: nowrap;
  }
  .invitation-panel .couple-name {
    top: 100px;
    font-size: 15px;
    letter-spacing: 2.6px;
  }
  .front-panel .couple-name {
    top: 314px;
    font-size: 27px;
    letter-spacing: 5px;
  }
  .wording {
    position: absolute;
    left: 0;
    right: 0;
    margin: 0;
    font-family: "Cormorant SC", serif;
    font-weight: 500;
    font-size: 13px;
    line-height: 15px;
    letter-spacing: 0.3px;
  }
  .hosts { top: 154px; }
  .request { top: 214px; }
  .date { top: 366px; }
  .ceremony { top: 397px; }
  .reception { top: 448px; }
  .rsvp { top: 535px; }
  .betrothed {
    position: absolute;
    left: 0;
    right: 0;
    top: 258px;
    margin: 0;
    font-family: "Pinyon Script", cursive;
    font-size: 40px;
    line-height: 30px;
    white-space: nowrap;
  }
  .betrothed .joiner {
    display: block;
    font-size: 22px;
    line-height: 16px;
  }
</style>
</head>
<body>
<main class="spread">
  <section class="invitation-panel">
    <svg class="monogram-mark" viewBox="0 0 56 56" aria-hidden="true">
      <circle cx="28" cy="28" r="26" fill="none" stroke="#1d1d1d" stroke-width="2"/>
    </svg>
    <h2 class="couple-name">NURIYA AND LAURENT</h2>

    <p class="wording hosts">Marcel and Yasmin Khoury<br>together with<br>Nikos and Elena Varga</p>
    <p class="wording request">Request with pleasure YOUR COMPANY<br>to celebrate the marriage of their children</p>

    <h1 class="betrothed">Nuriya Marcel Khoury<span class="joiner">and</span>Laurent Nikolas Varga</h1>

    <p class="wording date">Saturday 11th January 2014</p>
    <p class="wording ceremony">Saint Theodora Greek Orthodox Church<br>48 Linden Street, Westbrook<br>at 2.00pm</p>
    <p class="wording reception">A reception will follow at<br>Harbourview Hall<br>Shed 9, Ferry Pier<br>72 Quayside Promenade, Eastport<br>at 7.00pm</p>
    <p class="wording rsvp">Please RSVP by November 9, 2013<br>card enclosed</p>
  </section>

  <section class="front-panel">
    <svg class="monogram-mark" viewBox="0 0 164 164" aria-hidden="true">
      <circle cx="82" cy="82" r="78" fill="none" stroke="#1d1d1d" stroke-width="3"/>
    </svg>
    <h2 class="couple-name">NURIYA AND LAURENT</h2>
  </section>
</main>
</body>
</html>
```